The Brightpath Scholar, an online college fair for non-traditional students, needs a web site

I need design and coding for a functioning web site that will serve as an online college fair that connects non-traditional students with college admissions officers and college advisors. I have chosen Wordpress and the "Meridian" theme for the site, and you can see what I already have here: https://brightpathscholar.example/
I need help setting up the site's pages and functionality, including SEO optimization and a password protected area. I will manage all content. In addition to me as the administrator, other users will be: college admissions officers, non-traditional students (like homeschoolers), and college advisors.
Target Market(s)
Homeschoolers and college/university admissions officers
Industry/Entity Type
College
Coding
Coded - Design and coding required
Number of Pages Required
5+ page
Requirements
Must have
- - An inviting but professional look (see the logo as a starting point)
- - Easy to navigate
- - A way to register subscribed members (students)
- - A password-protected "members only" area
- - Virtual "booths" on the Schools page that lead to a detail page for each school
- - SEO optimized
Nice to have
- - Searchable site

```html
<!DOCTYPE html>
<html lang="en">
<head>
<meta charset="utf-8">
<title>The Brightpath Scholar – A Virtual College Fair</title>
<link rel="stylesheet" href="https://fonts.googleapis.com/css2?family=Open+Sans:wght@400;600;700&family=Roboto:wght@400;500;700&family=Roboto+Condensed:wght@400;700&display=swap">
<style>
:root{
  --navy:#0e2a4f;
  --navy-deep:#0a2142;
  --red:#d21f26;
  --red-dark:#b3141b;
  --ink:#2b2b2b;
  --muted:#6b6b6b;
  --line:#d9d9d9;
  --slate:#5b6b78;
  --paper:#ffffff;
  --soft:#f5f5f5;
}
*{box-sizing:border-box;margin:0;padding:0}
html,body{width:1200px;height:3689px;overflow:hidden}
body{position:relative;background:var(--paper);font-family:"Open Sans",Arial,sans-serif;color:var(--ink);font-size:13px;line-height:1.6}
.abs{position:absolute}
.ph{position:absolute}
h2.section-title{position:absolute;left:0;width:1200px;text-align:center;font-family:"Roboto",Arial,sans-serif;font-weight:400;font-size:31px;color:#222;letter-spacing:.5px}
.title-rule{position:absolute;left:564px;width:72px;height:3px;background:var(--red)}

/* header */
.site-header{position:absolute;left:0;top:0;width:1200px;height:135px;background:#fff}
.brand{position:absolute;left:98px;top:34px;display:flex;align-items:center;gap:12px}
.brand-mark{width:58px;height:58px;background:var(--red)}
.brand-name{font-family:"Roboto",Arial,sans-serif;font-weight:700;font-size:22px;color:var(--navy);line-height:1.1;width:190px}
.search{position:absolute;left:664px;top:46px;width:234px;height:38px;border:1px solid var(--line);display:flex}
.search span{flex:1;font-size:12px;color:#777;padding:9px 12px}
.search i{width:40px;background:#e3e3e3;display:flex;align-items:center;justify-content:center}
.auth-btn{position:absolute;top:46px;height:38px;border:2px solid var(--navy);border-radius:3px;font-size:13px;color:var(--navy);display:flex;align-items:center;gap:7px;padding:0 14px;font-weight:600}
.auth-btn b{width:10px;height:12px;background:var(--navy);border-radius:5px 5px 2px 2px}

/* nav */
.main-nav{position:absolute;left:0;top:135px;width:1200px;height:47px;background:var(--navy)}
.main-nav a{position:absolute;top:0;height:47px;line-height:47px;color:#fff;font-family:"Roboto",Arial,sans-serif;font-size:13px;font-weight:500;text-decoration:none;text-transform:uppercase}
.main-nav a.active{background:var(--red);padding:0 24px}

/* hero */
.hero{position:absolute;left:0;top:182px;width:1200px;height:548px;overflow:hidden}
.hero-photo{left:0;top:0;width:1200px;height:548px;background:linear-gradient(90deg,#5b3f27 0%,#8a6a48 25%,#b89874 48%,#caa888 62%,#6b5b53 80%,#3d3a44 100%)}
.hero h1{position:absolute;left:113px;top:168px;font-family:"Roboto",Arial,sans-serif;font-weight:700;font-size:34px;line-height:41px;color:#fff;text-transform:uppercase;width:480px}
.read-more{position:absolute;left:113px;top:310px;width:128px;height:42px;background:var(--navy);color:#fff;border-radius:3px;font-size:13px;font-weight:600;display:flex;align-items:center;justify-content:center;gap:6px}
.read-more i{width:11px;height:11px;border-radius:50%;background:#fff}
.slide-arrow{position:absolute;top:230px;width:36px;height:36px;border-radius:50%;background:rgba(0,0,0,.35);color:#fff;font-size:18px;text-align:center;line-height:34px}

/* services */
.service{position:absolute;top:843px;width:310px}
.service .ph{position:relative;width:310px;height:182px}
.service h3{font-family:"Roboto",Arial,sans-serif;font-weight:500;font-size:19px;margin-top:18px;color:#222;text-transform:uppercase}
.service p{font-size:12px;color:var(--muted);margin-top:8px;line-height:19px}

/* about */
.about-title{left:98px;top:1270px;font-family:"Roboto",Arial,sans-serif;font-size:31px;color:#222;text-transform:uppercase}
.about-rule{left:98px;top:1258px;width:72px;height:3px;background:var(--red)}
.about-intro{left:98px;top:1318px;width:490px;font-size:11.5px;color:var(--muted);line-height:19px}
.feature{position:absolute;left:98px;width:460px;display:flex;gap:20px}
.feature .ico{width:54px;height:54px;flex:none}
.feature h4{font-family:"Roboto",Arial,sans-serif;font-weight:500;font-size:15px;color:#9a9a9a;margin-bottom:6px}
.feature.lead h4{color:var(--red)}
.feature p{font-size:11.5px;color:var(--muted);line-height:18px}

/* schools */
.schools{position:absolute;left:0;top:1729px;width:1200px;height:558px;background:var(--slate)}
.school-card{position:absolute;top:150px;width:234px;height:300px;background:#fff}
.school-card .ph{position:relative;width:234px;height:228px}
.school-card h4{text-align:center;font-family:"Roboto",Arial,sans-serif;font-weight:700;font-size:19px;margin-top:12px;color:#222}
.school-card small{display:block;text-align:center;font-size:10px;font-style:italic;color:#555}
.dots{position:absolute;left:560px;top:489px;display:flex;gap:8px}
.dots i{width:9px;height:9px;border-radius:50%;background:#3c4855}
.dots i.on{background:#c9d0d6}

/* news */
.news{position:absolute;top:2422px;width:457px}
.news .ph{position:relative;width:457px;height:263px}
.news h3{font-family:"Roboto Condensed",Arial,sans-serif;font-weight:400;font-size:21px;color:#222;margin-top:22px}
.news .meta{font-size:11.5px;color:#555;margin-top:6px;display:flex;align-items:center;gap:8px}
.news .meta b{width:11px;height:11px;background:#666}
.news p{font-size:11.5px;color:#444;line-height:19px;margin-top:8px}
.news hr{border:none;border-top:1px solid #e2e2e2;margin-top:14px}

/* contact */
.contact{position:absolute;left:0;top:2919px;width:1200px;height:413px;background:linear-gradient(180deg,#ece8e1,#f3efe9 60%,#e9e5de)}
.field{position:absolute;background:#fff;border:1px solid #ddd;font-size:11px;color:#555;padding:10px 14px}
.submit{position:absolute;left:529px;top:322px;width:142px;height:37px;background:var(--red);color:#fff;border-radius:3px;font-family:"Roboto",Arial,sans-serif;font-weight:700;font-size:15px;text-align:center;line-height:37px}

/* footer */
.site-footer{position:absolute;left:0;top:3332px;width:1200px;height:312px;background:linear-gradient(180deg,#0e2a4f,#0b2447)}
.site-footer h5{position:absolute;top:46px;font-family:"Roboto",Arial,sans-serif;font-weight:400;font-size:17px;color:#fff;text-transform:uppercase}
.quick{position:absolute;left:98px;top:92px;list-style:none}
.quick li{font-size:12px;color:#fff;line-height:27px;display:flex;align-items:center;gap:12px}
.quick li::before{content:"";border-left:5px solid #fff;border-top:4px solid transparent;border-bottom:4px solid transparent}
.info{position:absolute;left:307px;width:240px;font-size:12px;color:#fff;line-height:18px;display:flex;gap:14px}
.info i{width:12px;height:12px;flex:none;margin-top:3px;background:#fff}
.info i.pin{border-radius:50% 50% 50% 0;transform:rotate(-45deg)}
.info i.round{border-radius:50%}
.news-text{position:absolute;left:626px;top:88px;width:290px;font-size:11.5px;color:#fff;line-height:19px}
.news-input{position:absolute;left:626px;top:149px;width:288px;height:42px;background:#fff;font-size:11px;color:#555;padding:12px 12px}
.news-btn{position:absolute;left:626px;top:204px;width:100px;height:40px;background:var(--red);color:#fff;font-size:12px;font-weight:600;text-align:center;line-height:40px}
.social{position:absolute;left:976px;list-style:none;top:90px}
.social li{display:flex;align-items:center;gap:10px;font-size:13px;color:#fff;height:36px}
.social li i{width:26px;height:26px;border:1.5px solid #fff;border-radius:50%}
.copyright{position:absolute;left:0;top:3644px;width:1200px;height:45px;background:var(--navy-deep);color:#fff;font-size:12px;text-align:center;line-height:45px}
</style>
</head>
<body>

<header class="site-header">
  <div class="brand"><div class="brand-mark"></div><div class="brand-name">The Brightpath Scholar</div></div>
  <div class="search"><span>Search</span><i><svg width="14" height="14" viewBox="0 0 14 14"><circle cx="6" cy="6" r="4.2" fill="none" stroke="#555" stroke-width="1.8"/><line x1="9" y1="9" x2="13" y2="13" stroke="#555" stroke-width="1.8"/></svg></i></div>
  <div class="auth-btn" style="left:919px"><b></b>Login</div>
  <div class="auth-btn" style="left:1005px"><b></b>Register</div>
</header>

<nav class="main-nav">
  <a class="active" style="left:98px">Home</a>
  <a style="left:219px">Students</a>
  <a style="left:339px">Schools</a>
  <a style="left:450px">Advisors</a>
  <a style="left:565px">Member Resources</a>
  <a style="left:747px">News</a>
  <a style="left:833px">Contact Us</a>
</nav>

<section class="hero">
  <div class="ph hero-photo" role="img" aria-label="Student with a tablet standing in a library with bookshelves behind her"></div>
  <h1>A Virtual College Fair for Non-Traditional Students</h1>
  <div class="read-more">READ MORE <i></i></div>
  <div class="slide-arrow" style="left:38px">&#8249;</div>
  <div class="slide-arrow" style="left:1128px">&#8250;</div>
  <svg class="abs" style="left:0;top:0" width="1200" height="548" viewBox="0 0 1200 548">
    <polygon points="0,510 590,548 1200,462 1200,548 0,548" fill="#fff"/>
    <polyline points="0,500 590,548 1200,460" fill="none" stroke="#d21f26" stroke-width="4"/>
  </svg>
</section>

<h2 class="section-title" style="top:774px">OUR SERVICES</h2>
<div class="title-rule" style="top:822px"></div>

<article class="service" style="left:98px">
  <div class="ph" role="img" aria-label="Group of students sitting on grass with laptops" style="background:linear-gradient(135deg,#6f8a45,#9bb06a 50%,#3f4f3a)"></div>
  <h3>Students</h3>
  <p>Sed ut perspiciatis unde omnis iste natus error sit voluptatem accusantium doloremque laudantium, totam rem aperiam, eaque ipsa quae ab</p>
</article>
<article class="service" style="left:445px">
  <div class="ph" role="img" aria-label="Smiling student with a backpack outdoors" style="background:linear-gradient(135deg,#5e8f2e,#8fbf4a 55%,#3d6a24)"></div>
  <h3>Schools</h3>
  <p>Sed ut perspiciatis unde omnis iste natus error sit voluptatem accusantium doloremque laudantium, totam rem aperiam, eaque ipsa quae ab</p>
</article>
<article class="service" style="left:789px">
  <div class="ph" role="img" aria-label="Advisor speaking to a lecture hall of students" style="background:linear-gradient(135deg,#8c6a4a,#b98f66 50%,#4a3a33)"></div>
  <h3>Advisors</h3>
  <p>Sed ut perspiciatis unde omnis iste natus error sit voluptatem accusantium doloremque laudantium, totam rem aperiam, eaque ipsa quae ab</p>
</article>

<div class="abs" style="left:0;top:1193px;width:1200px;height:1px;background:#ececec"></div>
<div class="abs about-rule"></div>
<h2 class="abs about-title">About Us</h2>
<p class="abs about-intro">Sed ut perspiciatis unde omnis iste natus error sit voluptatem accusantium doloremque laudantium, totam rem aperiam, eaque ipsa quae ab illo inventore veritatis et quasi architecto beatae vitae dicta sunt explicabo. Nemo enim ipsam voluptatem quia</p>

<div class="feature lead" style="top:1398px">
  <svg class="ico" viewBox="0 0 54 54"><rect x="10" y="10" width="34" height="34" transform="rotate(45 27 27)" fill="#d21f26"/><path d="M20 30 L27 22 L34 30 Z" fill="#fff"/></svg>
  <div><h4>Welcome To The Brightpath Scholar</h4><p>Sed ut perspiciatis unde omnis iste natus error sit voluptatem accusantium doloremque laudantium, totam rem...</p></div>
</div>
<div class="feature" style="top:1490px">
  <svg class="ico" viewBox="0 0 54 54"><rect x="10" y="10" width="34" height="34" transform="rotate(45 27 27)" fill="#b5b5b5"/><path d="M21 27 L26 32 L34 22" fill="none" stroke="#fff" stroke-width="3"/></svg>
  <div><h4>Contest and Programs</h4><p>Sed ut perspiciatis unde omnis iste natus error sit voluptatem accusantium doloremque laudantium, totam rem...</p></div>
</div>
<div class="feature" style="top:1581px">
  <svg class="ico" viewBox="0 0 54 54"><rect x="10" y="10" width="34" height="34" transform="rotate(45 27 27)" fill="#b5b5b5"/><circle cx="27" cy="27" r="6" fill="none" stroke="#fff" stroke-width="3"/></svg>
  <div><h4>Support To All Colleges</h4><p>Sed ut perspiciatis unde omnis iste natus error sit voluptatem accusantium doloremque laudantium, totam rem...</p></div>
</div>
<div class="ph" role="img" aria-label="Two students sitting on the floor looking at a laptop" style="left:602px;top:1254px;width:522px;height:406px;background:radial-gradient(ellipse at 55% 55%,#9bb0c6 0%,#c9cfd6 35%,#f2f2f2 70%,#fff 100%)"></div>

<section class="schools">
  <h2 class="section-title" style="top:40px;color:#fff">MEET OUR SCHOOLS</h2>
  <div class="title-rule" style="top:98px"></div>
  <div class="school-card" style="left:98px"><div class="ph" role="img" aria-label="Portrait of a school representative" style="background:linear-gradient(180deg,#6b4a3c,#a47b63)"></div><h4>RUBY</h4><small>CEO-Lorum ipsum</small></div>
  <div class="school-card" style="left:354px"><div class="ph" role="img" aria-label="Portrait of a school representative" style="background:linear-gradient(180deg,#6e5a4c,#3a3a40)"></div><h4>RUBY</h4><small>CEO-Lorum ipsum</small></div>
  <div class="school-card" style="left:610px"><div class="ph" role="img" aria-label="Portrait of a school representative" style="background:linear-gradient(180deg,#8a6b5e,#b73a3a)"></div><h4>RUBY</h4><small>CEO-Lorum ipsum</small></div>
  <div class="school-card" style="left:866px"><div class="ph" role="img" aria-label="Portrait of a school representative" style="background:linear-gradient(180deg,#7a6a5e,#3e4754)"></div><h4>RUBY</h4><small>CEO-Lorum ipsum</small></div>
  <div class="dots"><i></i><i class="on"></i><i></i><i></i></div>
</section>

<h2 class="section-title" style="top:2338px">LATEST NEWS</h2>
<article class="news" style="left:118px">
  <div class="ph" role="img" aria-label="Student in a red jacket using a laptop on the phone" style="background:linear-gradient(135deg,#c8c2b6,#b2372f 45%,#e6e2da)"></div>
  <h3>Here's a sneak peek at what we're working on....!</h3>
  <div class="meta"><b></b>September 29, 2016 by Dana Whitfield</div>
  <p>The Brightpath Scholar is a new web site designed to provide a meeting place for college and university admissions officers and non-traditional applicants like homeschoolers, unschoolers, students who attend</p>
  <hr>
</article>
<article class="news" style="left:622px">
  <div class="ph" role="img" aria-label="Student sitting on grass with a laptop in a park" style="background:linear-gradient(180deg,#5f7d3a,#8fb35a 55%,#6c9a3a)"></div>
  <h3>Here's a sneak peek at what we're working on....!</h3>
  <div class="meta"><b></b>September 29, 2016 by Dana Whitfield</div>
  <p>The Brightpath Scholar is a new web site designed to provide a meeting place for college and university admissions officers and non-traditional applicants like homeschoolers, unschoolers, students who attend</p>
  <hr>
</article>

<section class="contact">
  <h2 class="section-title" style="top:62px">CONTACT US</h2>
  <div class="field" style="left:266px;top:137px;width:325px;height:40px">Name :</div>
  <div class="field" style="left:266px;top:189px;width:325px;height:40px">Phone :</div>
  <div class="field" style="left:266px;top:242px;width:325px;height:40px">Email :</div>
  <div class="field" style="left:610px;top:137px;width:325px;height:145px">Message :</div>
  <div class="submit">SUBMIT</div>
</section>

<footer class="site-footer">
  <h5 style="left:98px">Quick Links</h5>
  <ul class="quick"><li>Home</li><li>Students</li><li>Schools</li><li>Advisors</li><li>Member Resources</li><li>News</li><li>Contact Us</li></ul>
  <h5 style="left:307px">Contact Info</h5>
  <div class="info" style="top:93px"><i class="pin"></i><span>The Brightpath Scholar 14 Elm Row<br>20410 Lakeside</span></div>
  <div class="info" style="top:144px"><i class="round"></i><span>Phone : (+111) 555-0142</span></div>
  <div class="info" style="top:182px"><i></i><span>Email: info@brightpathscholar.example</span></div>
  <h5 style="left:626px">Join Our Newsletter</h5>
  <p class="news-text">Excepteur sint occaecat cupidatat non proident, sunt in culpa qui</p>
  <div class="news-input">Enter Name</div>
  <div class="news-btn">SUBSCRIBE</div>
  <h5 style="left:976px">Social Media</h5>
  <ul class="social"><li><i></i>Social Page</li><li><i></i>Updates Feed</li><li><i></i>Career Profile</li><li><i></i>Video Channel</li></ul>
</footer>
<div class="copyright">© 2017 The Brightpath Scholar. All Rights Reserved.</div>

</body>
</html>
```